New product logo and packaging design for brand ( Nestwell & Rinse)

I need a logo and packaging design for 2 new products that will look similar. One is eco friendly dishwashing sheets and the other is a eco friendly dishwashing sheets.
The descriptions that go on the boxes have all ready been written and I have uploaded for you to utilise on the back of the box,. Please search eco washing sheets on google for brand references.
The look should be upmarket but yet show to be eco friendly. The brand will be called Nestwell & Rinse. Feel free to let your creative juices flow and make something you believe would work well and doesn't look like our competitors. It should look clean yet incorporate something natural with an animal.
I like the artwork for https://velmorastone.example/ but don't make it look the same.
Possibly the outline of the planet earth inside the letter O in nestwell & rinse logo.

The laundry sheets are:
OCEAN BREEZE

The Dishwasher sheets are:
LEMON
I repeat , they should NOT look like the competitors.

Must use the template for the design in the attached files!

On the front should say - 80 Sheets

There will be a second contest I will post now that will be the same project under a different name you can search it and enter both if you would like, they will be sold at different price points to attract different customers.

I have uploaded a new template , the manufacturer gave me the wrong template please update asap

Washing clothes

• use the template for the design in the attached files

```html
<!DOCTYPE html>
<html lang="en">
<head>
<meta charset="utf-8">
<title>Nestwell &amp; Rinse – Lemon Dishwashing Sheets dieline</title>
<link rel="stylesheet" href="https://fonts.googleapis.com/css2?family=Quicksand:wght@400;500;600;700&family=Cormorant+Garamond:wght@300;500&display=swap">
<style>
  :root{
    --stage:#b3b1b2;
    --paper:#ffffff;
    --green:#4c7032;
    --green-dark:#344c3a;
    --cream:#f9dfb0;
    --cream-text:#f6e6bb;
    --orange:#f2b01e;
    --yellow:#eec42c;
    --cut:#1e1e1e;
    --dim:#e0141b;
    --sans:"Quicksand", sans-serif;
    --serif:"Cormorant Garamond", serif;
  }
  html,body{margin:0;padding:0;width:1200px;height:1200px;overflow:hidden;background:var(--stage);}
  .sheet{position:relative;width:1932px;height:1932px;transform:scale(0.62112);transform-origin:0 0;font-family:var(--sans);}
  .dieline{position:absolute;left:0;top:0;}
  .block{position:absolute;color:var(--cream-text);font-size:11.6px;line-height:14.7px;font-weight:500;letter-spacing:-.1px;}
  .block h3{margin:0;font-size:11.6px;font-weight:700;letter-spacing:.1px;}
  .block p{margin:0;}
  .justify{text-align:justify;}
  .bold{font-weight:700;}
  .contact{position:absolute;top:876px;display:flex;align-items:center;gap:6px;color:var(--cream-text);font-weight:700;font-size:12px;}
  .contact .mark{width:13px;height:13px;border:1.4px solid var(--cream-text);border-radius:3px;box-sizing:border-box;}
  .storage{left:725px;top:934px;width:440px;font-weight:700;}
  .brand{position:absolute;left:806px;top:1108px;width:172px;text-align:right;font-family:var(--sans);font-weight:700;color:var(--green);font-size:17px;line-height:24px;white-space:nowrap;}
  .product-tag{position:absolute;left:985px;top:1099px;width:261px;height:42px;background:var(--green);color:var(--cream);font-size:21px;font-weight:500;letter-spacing:.8px;display:flex;align-items:center;justify-content:center;}
  .flavour{position:absolute;left:922px;top:1222px;font-family:var(--serif);font-weight:500;font-size:66px;letter-spacing:10px;color:var(--green);line-height:1;}
  .count{position:absolute;left:1222px;top:1262px;font-family:var(--serif);font-weight:300;font-size:78px;color:var(--green);line-height:1;}
  .count-label{position:absolute;left:1226px;top:1333px;width:71px;height:21px;background:var(--green);color:var(--cream);font-size:16px;font-weight:500;display:flex;align-items:center;justify-content:center;letter-spacing:.5px;}
  .claims{position:absolute;left:820px;top:1452px;width:468px;height:40px;background:var(--yellow);display:flex;gap:12px;padding:4px 14px;box-sizing:border-box;color:#8a6a1a;font-size:7px;line-height:9px;}
  .claims p{margin:0;flex:1;}
  .claims p:first-child{text-align:justify;}
  .dim-label{position:absolute;color:var(--dim);font-family:Arial,sans-serif;font-size:36px;line-height:1;}
  .dim-label.vertical{transform:rotate(-90deg);transform-origin:center;}
</style>
</head>
<body>
<main class="sheet">
  <svg class="dieline" width="1932" height="1932" viewBox="0 0 1932 1932" xmlns="http://www.w3.org/2000/svg">
    <defs>
      <pattern id="glue-hatch" width="22" height="22" patternUnits="userSpaceOnUse" patternTransform="rotate(45)">
        <rect width="22" height="22" fill="#fff"/>
        <line x1="0" y1="0" x2="0" y2="22" stroke="#1e1e1e" stroke-width="2"/>
      </pattern>
    </defs>

    <!-- paper sheet -->
    <polygon points="533,340 706,470 706,1512 533,1512" fill="var(--paper)"/>
    <polygon points="1573,340 1401,470 1401,1512 1573,1512" fill="var(--paper)"/>

    <!-- hanger lid -->
    <polygon points="724,331 1383,331 1401,469 706,469" fill="var(--green)" stroke="var(--cut)" stroke-width="1.2"/>
    <rect x="729" y="422" width="211" height="31" fill="url(#glue-hatch)"/>
    <rect x="1170" y="422" width="203" height="31" fill="url(#glue-hatch)"/>
    <path d="M970,401 L1032,401 C1036,390 1046,388 1053,388 C1060,388 1070,390 1074,401 L1137,401 A6,6 0 0 1 1137,413 L970,413 A6,6 0 0 1 970,401 Z" fill="none" stroke="var(--cut)" stroke-width="1.2"/>

    <!-- back panel and its side flaps -->
    <rect x="706" y="469" width="695" height="444" fill="var(--green)" stroke="var(--cut)" stroke-width="1.2"/>
    <polygon points="706,469 690,477 625,477 557,489 557,895 625,905 690,905 706,913" fill="var(--green)" stroke="var(--cut)" stroke-width="1.2"/>
    <polygon points="1401,469 1417,477 1482,477 1550,489 1550,895 1482,905 1417,905 1401,913" fill="var(--green)" stroke="var(--cut)" stroke-width="1.2"/>
    <rect x="656" y="496" width="31" height="390" fill="url(#glue-hatch)" stroke="var(--cut)"/>
    <rect x="1421" y="496" width="31" height="390" fill="url(#glue-hatch)" stroke="var(--cut)"/>

    <!-- top band -->
    <rect x="555" y="913" width="997" height="155" fill="var(--cream)"/>
    <rect x="706" y="913" width="695" height="155" fill="var(--green)" stroke="var(--cut)" stroke-width="1.2"/>
    <path d="M706,913 L690,921 L640,921 C602,921 571,952 571,990 C571,1029 602,1060 640,1060 L690,1060 L706,1068" fill="none" stroke="var(--cut)" stroke-width="1.2"/>
    <path d="M1401,913 L1417,921 L1467,921 C1505,921 1536,952 1536,990 C1536,1029 1505,1060 1467,1060 L1417,1060 L1401,1068" fill="none" stroke="var(--cut)" stroke-width="1.2"/>
    <rect x="1189" y="941" width="167" height="51" rx="12" fill="var(--green-dark)"/>
    <rect x="1188" y="998" width="168" height="52" fill="#f5f5f5"/>

    <!-- front panel -->
    <rect x="555" y="1068" width="997" height="444" fill="var(--cream)"/>
    <path d="M706,1068 L690,1076 L653,1076 L555,1088 L555,1500 L653,1503 L690,1503 L706,1512" fill="none" stroke="var(--cut)" stroke-width="1.2"/>
    <path d="M1401,1068 L1417,1076 L1454,1076 L1552,1088 L1552,1500 L1454,1503 L1417,1503 L1401,1512" fill="none" stroke="var(--cut)" stroke-width="1.2"/>
    <line x1="706" y1="1068" x2="706" y2="1665" stroke="var(--cut)" stroke-width="1.2"/>
    <line x1="1401" y1="1068" x2="1401" y2="1665" stroke="var(--cut)" stroke-width="1.2"/>
    <line x1="706" y1="1068" x2="1401" y2="1068" stroke="var(--cut)" stroke-width="1.2"/>
    <path d="M775,1078 L775,1400 C775,1440 790,1480 815,1512" fill="none" stroke="var(--cut)" stroke-width="1.2"/>
    <path d="M795,1078 L795,1400 C795,1440 805,1480 815,1500" fill="none" stroke="var(--cut)" stroke-width="1.2"/>
    <path d="M1331,1078 L1331,1400 C1331,1440 1316,1480 1292,1512" fill="none" stroke="var(--cut)" stroke-width="1.2"/>
    <path d="M1313,1078 L1313,1400 C1313,1440 1303,1480 1292,1500" fill="none" stroke="var(--cut)" stroke-width="1.2"/>

    <!-- bottom tuck band -->
    <rect x="555" y="1512" width="997" height="153" fill="var(--orange)"/>
    <line x1="706" y1="1512" x2="1401" y2="1512" stroke="var(--cut)" stroke-width="1.2"/>
    <path d="M706,1512 L690,1520 L640,1520 C602,1520 571,1551 571,1589 C571,1627 602,1657 640,1657 L690,1657 L706,1665" fill="none" stroke="var(--cut)" stroke-width="1.2"/>
    <path d="M1401,1512 L1417,1520 L1467,1520 C1505,1520 1536,1551 1536,1589 C1536,1627 1505,1657 1467,1657 L1417,1657 L1401,1665" fill="none" stroke="var(--cut)" stroke-width="1.2"/>
    <path d="M706,1665 L935,1665 C955,1665 968,1650 980,1636 L984,1650 C987,1660 995,1665 1006,1665 L1100,1665 C1111,1665 1119,1660 1122,1650 L1127,1636 C1140,1650 1152,1665 1172,1665 L1401,1665" fill="none" stroke="var(--cut)" stroke-width="1.2"/>
    <path d="M815,1512 L815,1600 Q815,1610 826,1610 L960,1610 Q975,1610 980,1636 M1127,1636 Q1133,1610 1148,1610 L1282,1610 Q1292,1610 1292,1600 L1292,1512" fill="none" stroke="var(--cut)" stroke-width="1.2" stroke-dasharray="26 10"/>

    <!-- back panel simple diagrams -->
    <g role="img" aria-label="Line illustration of a dishwasher">
      <rect x="790" y="572" width="87" height="64" fill="none" stroke="var(--cream-text)" stroke-opacity=".55" stroke-width="1.2" rx="4"/>
    </g>
    <g aria-label="Sheet torn in half" role="img">
      <rect x="1012" y="581" width="82" height="42" fill="none" stroke="var(--cream-text)" stroke-width="1.2"/>
      <line x1="1053" y1="575" x2="1053" y2="630" stroke="var(--cream-text)" stroke-width="1.2" stroke-dasharray="4 4"/>
    </g>
    <g role="img" aria-label="Line illustration of a sheet dissolving in a bowl">
      <rect x="1244" y="560" width="54" height="61" fill="none" stroke="var(--cream-text)" stroke-opacity=".55" stroke-width="1.2" rx="4"/>
    </g>
    <rect x="1232" y="749" width="79" height="79" fill="var(--cream)"/>
    <rect x="1237" y="754" width="14" height="14" fill="var(--orange)"/>
    <rect x="1292" y="754" width="14" height="14" fill="var(--orange)"/>
    <rect x="1237" y="809" width="14" height="14" fill="var(--orange)"/>
    <rect x="1292" y="809" width="14" height="14" fill="var(--orange)"/>

    <!-- front decorations -->
    <path role="img" aria-label="Lemon slice line illustration" d="M1080,1232 A83,83 0 0 1 1245,1232 Z" fill="#eed39a" stroke="var(--green)" stroke-width="1"/>
    <path role="img" aria-label="Lemon slice line illustration" d="M862,1286 A83,83 0 0 0 1027,1286 Z" fill="#eed39a" stroke="var(--green)" stroke-width="1"/>
    <circle role="img" aria-label="Badge: tough on grease" cx="886" cy="1400" r="46" fill="#efd49c"/>
    <circle role="img" aria-label="Badge: gentle on the environment" cx="1054" cy="1400" r="46" fill="#efd49c"/>
    <circle role="img" aria-label="Badge: simple, clean and convenient" cx="1220" cy="1400" r="46" fill="#efd49c"/>

    <!-- dimensions -->
    <g stroke="var(--dim)" stroke-width="1.4" fill="none">
      <line x1="452" y1="331" x2="452" y2="1665"/>
      <line x1="447" y1="331" x2="519" y2="331"/>
      <line x1="447" y1="469" x2="519" y2="469"/>
      <line x1="447" y1="913" x2="527" y2="913"/>
      <line x1="447" y1="1068" x2="521" y2="1068"/>
      <line x1="447" y1="1512" x2="524" y2="1512"/>
      <line x1="447" y1="1665" x2="522" y2="1665"/>
      <line x1="555" y1="1770" x2="1552" y2="1770"/>
      <line x1="555" y1="1700" x2="555" y2="1775"/>
      <line x1="706" y1="1700" x2="706" y2="1775"/>
      <line x1="1401" y1="1694" x2="1401" y2="1775"/>
      <line x1="1552" y1="1694" x2="1552" y2="1775"/>
    </g>
  </svg>

  <!-- back panel copy -->
  <section class="block justify" style="left:725px;top:486px;width:213px;">
    <h3>HOW TO USE</h3>
    <h3 style="margin-top:4px;">For Dishwashers:</h3>
    <p>• Place a single sheet into your dishwasher's detergent compartment and let it do the work.</p>
  </section>
  <section class="block" style="left:725px;top:643px;width:215px;">
    <h3>LOAD SIZE GUIDE</h3>
    <p style="white-space:nowrap;">• One sheet for full loads or handwashing.</p>
  </section>
  <section class="block justify" style="left:725px;top:712px;width:213px;">
    <h3>EARTH-FRIENDLY FORMULA</h3>
    <p>• Free from harsh chemicals like phos­phates, dyes, and bleach</p>
    <p>• Safe for septic tanks and greywater systems</p>
    <p>• 100% plastic-free, biodegradable packaging</p>
    <p>• Made with eco-friendly ingredients</p>
    <h3 style="margin-top:3px;">GET IN TOUCH</h3>
    <p class="bold" style="white-space:nowrap;">We love hearing from you! Reach out with your questions or feedback:</p>
  </section>

  <section class="block" style="left:950px;top:504px;width:208px;">
    <h3>For Dish Drawers:</h3>
    <p>• Tear a sheet in half and place it in the cutlery tray. If you see extra foam, use less next time.</p>
  </section>
  <section class="block" style="left:950px;top:642px;width:208px;">
    <h3>WHAT'S INSIDE</h3>
    <p class="bold justify">We use natural, plant-based ingre­dients such as:</p>
    <p style="font-size:10.6px;line-height:13px;">• Sodium Dodecyl Sulphate<br>• Aqua<br>• Decyl Glucoside<br>• PEG-7 Glyceryl Cocoate<br>• Cocamidopropyl Betaine<br>• Cocamidopropylamine Oxide<br>• Coconut Oil Monoethanolamide<br>• Glycerin<br>• Alcohols, C12-18, Ethoxylated<br>• Perfume<br>• Sodium Carbonate</p>
  </section>

  <section class="block" style="left:1169px;top:504px;width:212px;">
    <h3>For Hand Washing:</h3>
    <p>• Add one sheet to warm water, let it dissolve, and wash dishes as usual</p>
  </section>
  <section class="block justify" style="left:1169px;top:642px;width:212px;">
    <h3>OUR PROMISE</h3>
    <p>At Nestwell &amp; Rinse, we're proud to be an Australian-owned business commi­tted to sustainability. By switching to our dishwashing sheets, you're helping to protect the environment one load at a time.</p>
  </section>

  <div class="contact" style="left:743px;"><span class="mark"></span>support@nestwellrinse.example</div>
  <div class="contact" style="left:1001px;"><span class="mark"></span>www.nestwellrinse.example</div>
  <div class="contact" style="left:1251px;"><span class="mark"></span>@nestwellrinse</div>

  <!-- storage panel -->
  <section class="block storage">
    <h3>STORAGE AND SHELF LIFE</h3>
    <p style="margin-top:15px;">• Store in a cool, dry place away from direct sunlight.<br>• Close the box tightly after each use to maintain freshness.<br>• Shelf life: 2 years from the production date (see box for details).</p>
    <p style="margin-top:15px;">CAUTION: Do not ingest. Keep out of eyes. If contact occurs, rinse thorou­ghly and seek medical attention if necessary.</p>
  </section>

  <!-- front panel -->
  <div class="brand">Nestwell &amp; Rinse</div>
  <div class="product-tag">DISHWASHING SHEETS</div>
  <div class="flavour">LEMON</div>
  <div class="count">80</div>
  <div class="count-label">SHEETS</div>
  <div class="claims">
    <p>Harness the power of plant-based enzymes to break down stubborn grease and grime, leaving your dishes spotless without harmful residues.</p>
    <p>Ditch messy liquids and bulky pods—our sheets are an easy-to-use, space-saving solution that gets the job done with zero fuss.</p>
  </div>

  <!-- dimension labels -->
  <div class="dim-label vertical" style="left:393px;top:413px;">35,5</div>
  <div class="dim-label vertical" style="left:403px;top:700px;">115</div>
  <div class="dim-label vertical" style="left:412px;top:990px;">40</div>
  <div class="dim-label vertical" style="left:403px;top:1300px;">115</div>
  <div class="dim-label vertical" style="left:393px;top:1578px;">39,5</div>
  <div class="dim-label" style="left:605px;top:1716px;">39</div>
  <div class="dim-label" style="left:1018px;top:1716px;">180</div>
  <div class="dim-label" style="left:1451px;top:1716px;">39</div>
</main>
</body>
</html>
```